Flyer for Aluminium recycling business

We are a startup aluminium recycling business. We don’t have a logo yet. I’ve attached a flyer created by one of our sales people but it’s a bit average and we need something a bit more modern and slick. You have creative license to completely change everything - as long as the information being communicated is the same.

Target Market(s)

Hospitality, Hotels, Apartment blocks, malls etcs

Industry/Entity Type

Aluminium recycling

Requirements
Must have
• the wording
Nice to have
• you have free license on design aspect

```html
<!DOCTYPE html>
<html lang="en">
<head>
<meta charset="utf-8">
<title>Circular Reclaim – Aluminium Recycling Flyer</title>
<link href="https://fonts.googleapis.com/css2?family=Montserrat:wght@400;600;700&family=Fira+Sans:wght@600&display=swap" rel="stylesheet">
<style>
  :root{
    --page:#ffffff;
    --navy:#0b1f38;
    --band:#243a52;
    --white:#ffffff;
    --green:#3ac93a;
    --belt:#c9ced6;
    --collect:#7fb3d3; --collect-label:#3f88b5;
    --sort:#cfe06a;    --sort-label:#a5b82a;
    --crush:#ffb95a;   --crush-label:#f39200;
    --melt:#5fe0c0;    --melt-label:#1fa383;
    --cast:#f4d25e;    --cast-label:#f0bd14;
  }
  *{box-sizing:border-box;margin:0;padding:0}
  html,body{width:1200px;height:1200px;overflow:hidden;background:var(--page)}
  body{font-family:"Montserrat",sans-serif;color:var(--white);position:relative}

  .flyer{position:absolute;left:210px;top:47px;width:787px;height:1114px;background:var(--navy);overflow:hidden}
  .flyer > *{position:absolute}

  .brand-mark{left:60px;top:52px;width:116px;height:116px;border-radius:50%;background:var(--green)}
  .brand-name{left:215px;top:50px;font-weight:700;font-size:62px;line-height:66px;letter-spacing:0.5px}

  .tagline{left:0;width:100%;text-align:center;font-weight:700;font-size:21px;padding-left:26px}
  .tagline--lead{top:211px;line-height:22px}
  .tagline--promise{top:249px;line-height:28px}

  .section-title{left:0;width:100%;text-align:center;font-weight:700;font-size:25px;line-height:26px}
  .section-title--steps{top:337px}
  .section-title--items{top:819px}

  .band{left:0;width:100%;background:var(--band)}
  .band--steps{top:372px;height:192px}
  .band--process{top:581px;height:219px}
  .band--items{top:866px;height:156px}

  .point-list{list-style:none;font-size:17px;line-height:23px;font-weight:400;letter-spacing:0.2px}
  .point-list li{position:relative;padding-left:0}
  .point-list li.dot::before{content:"•";position:absolute;left:-36px;font-size:10px}
  .point-list--steps{left:91px;top:387px;width:640px}
  .point-list--items{left:88px;top:873px;width:640px}

  .stage{top:582px;width:110px;height:135px;border:1px solid var(--c);border-bottom:none;border-radius:4px 4px 0 0;overflow:hidden}
  .stage__art{width:100%;height:100%;background:linear-gradient(to bottom,var(--c) 0,rgba(36,58,82,0) 26px,rgba(36,58,82,0) 30px),
      radial-gradient(ellipse at 50% 60%,var(--c) 0,transparent 62%);opacity:.85}
  .stage--collect{left:87px;--c:var(--collect)}
  .stage--sort{left:214px;--c:var(--sort)}
  .stage--crush{left:342px;--c:var(--crush)}
  .stage--melt{left:469px;--c:var(--melt)}
  .stage--cast{left:597px;--c:var(--cast)}

  .belt{left:75px;top:719px;width:643px;height:17px;border-radius:9px;background:var(--belt);display:flex;align-items:center;justify-content:space-between;padding:0 4px}
  .belt span{width:10px;height:10px;border-radius:50%;border:2px solid var(--band);background:var(--belt)}

  .stage-label{top:742px;width:110px;height:53px;border-radius:3px;display:flex;align-items:center;justify-content:center;text-align:center;
    font-family:"Fira Sans",sans-serif;font-weight:600;font-size:12.5px;line-height:15px}
  .stage-label--collect{left:87px;background:var(--collect-label)}
  .stage-label--sort{left:214px;background:var(--sort-label)}
  .stage-label--crush{left:342px;background:var(--crush-label)}
  .stage-label--melt{left:469px;background:var(--melt-label)}
  .stage-label--cast{left:597px;background:var(--cast-label)}

  .contact-phone{left:49px;top:1036px;font-weight:700;font-size:48px;line-height:48px}
  .contact-email{right:56px;top:1051px;font-size:17px;line-height:18px;letter-spacing:0.3px}
</style>
</head>
<body>
<main class="flyer">
  <div class="brand-mark"></div>
  <h1 class="brand-name">CIRCULAR<br>RECLAIM</h1>

  <p class="tagline tagline--lead">Playing the fair aluminium recycling game for good</p>
  <p class="tagline tagline--promise">Our partnership with you is based on common sense,<br>mutual gain and a better tomorrow</p>

  <h2 class="section-title section-title--steps">IT'S SIMPLE:</h2>
  <div class="band band--steps"></div>
  <ul class="point-list point-list--steps">
    <li class="dot">We bring you a free bin</li>
    <li class="dot">You throw all and any aluminium waste into the bin - no need to super-clean it. Try to compact/squash the aluminium as much as possible</li>
    <li class="dot">We collect the bin at no charge</li>
    <li class="dot">We turn the aluminium waste into a desirable resource</li>
    <li>We pay you for however much of that resource your waste has generated - and give you a report on that, so you can see how good you are</li>
  </ul>

  <div class="band band--process"></div>
  <div class="stage stage--collect"><div class="stage__art" role="img" aria-label="Illustration of a crane collecting scrap metal"></div></div>
  <div class="stage stage--sort"><div class="stage__art" role="img" aria-label="Illustration of a pile of sorted scrap pieces"></div></div>
  <div class="stage stage--crush"><div class="stage__art" role="img" aria-label="Illustration of a press crushing scrap between rollers"></div></div>
  <div class="stage stage--melt"><div class="stage__art" role="img" aria-label="Illustration of scrap being remelted in a furnace"></div></div>
  <div class="stage stage--cast"><div class="stage__art" role="img" aria-label="Illustration of molten metal poured from a ladle"></div></div>
  <div class="belt"><span></span><span></span><span></span><span></span><span></span><span></span><span></span><span></span><span></span></div>
  <div class="stage-label stage-label--collect">Collecting<br>Scrap</div>
  <div class="stage-label stage-label--sort">Sorting<br>Scrap</div>
  <div class="stage-label stage-label--crush">Crushing</div>
  <div class="stage-label stage-label--melt">Remelting</div>
  <div class="stage-label stage-label--cast">Secondary<br>Casting</div>

  <h2 class="section-title section-title--items">EXAMPLES OF WHAT WE CAN TAKE:</h2>
  <div class="band band--items"></div>
  <ul class="point-list point-list--items">
    <li class="dot">Used beverage cans - any</li>
    <li class="dot">Tinfoil-scrunched, crusty, burned or dirty</li>
    <li>Disposable BBQ roasting trays</li>
    <li class="dot">Aluminium takeaway containers</li>
    <li class="dot">Wine bottle screw tops (and collars - if you can get them off)</li>
    <li class="dot">Tear-off can lids</li>
  </ul>

  <p class="contact-phone">021 555 0142</p>
  <p class="contact-email">join@circularreclaim.co.nz</p>
</main>
</body>
</html>
```